Vellum Systemics Buisness Cards

I need a technology focused clean business card for my employees. I have attached out logo to include in the mocks. We're a modern tech consulting firm that drives to interface humanity with technology in a truly cohesive fashion.

```html
<!DOCTYPE html>
<html lang="en">
<head>
<meta charset="UTF-8">
<title>Vellum Systemics Business Cards</title>
<link href="https://fonts.googleapis.com/css2?family=Roboto:wght@400;500;700&family=Roboto+Condensed:wght@500;700&display=swap" rel="stylesheet">
<style>
  :root {
    --brand-blue: #1c75bc;
    --brand-grey: #7b7c7f;
    --text-grey: #5b5c5e;
    --card-white: #f3f3f3;
    --stage: #e4e4e2;
  }
  * { margin: 0; padding: 0; box-sizing: border-box; }
  html, body { width: 1200px; height: 960px; overflow: hidden; }
  body {
    background: var(--stage);
    font-family: "Roboto", Arial, sans-serif;
    position: relative;
  }
  .card {
    position: absolute;
    width: 600px;
    height: 343px;
    box-shadow: 0 2px 6px rgba(0,0,0,0.25);
    overflow: hidden;
  }
  .card-front { left: 314px; top: 113px; background: var(--card-white); }
  .card-back { left: 312px; top: 472px; background: var(--brand-blue); }

  .front-bands { position: absolute; inset: 0; }

  .brand-lockup {
    position: absolute;
    left: 58px;
    top: 152px;
    display: flex;
    align-items: center;
    gap: 10px;
  }
  .brand-dot {
    width: 16px; height: 16px;
    border-radius: 50%;
    background: var(--brand-blue);
  }
  .brand-name {
    font-family: "Roboto", Arial, sans-serif;
    font-weight: 500;
    font-size: 28px;
    color: var(--brand-grey);
    letter-spacing: 0.5px;
  }

  .divider {
    position: absolute;
    left: 339px;
    top: 72px;
    width: 1px;
    height: 200px;
    background: linear-gradient(to bottom, rgba(150,150,150,0), rgba(150,150,150,0.8) 20%, rgba(150,150,150,0.8) 80%, rgba(150,150,150,0));
  }

  .contact-block { position: absolute; left: 369px; top: 74px; }
  .person-name {
    font-family: "Roboto Condensed", Arial, sans-serif;
    font-weight: 700;
    font-size: 21px;
    color: var(--brand-blue);
    line-height: 22px;
  }
  .person-title {
    font-family: "Roboto Condensed", Arial, sans-serif;
    font-weight: 500;
    font-size: 15px;
    color: var(--brand-grey);
    line-height: 18px;
    margin-top: 1px;
  }
  .address {
    margin-top: 19px;
    font-size: 14px;
    line-height: 18px;
    color: var(--text-grey);
  }
  .contact-list { list-style: none; margin-top: 15px; }
  .contact-list li {
    display: flex;
    align-items: center;
    gap: 9px;
    font-size: 14px;
    line-height: 19px;
    color: var(--text-grey);
  }
  .contact-list svg { width: 13px; height: 13px; fill: var(--brand-blue); flex: none; }

  .back-lockup {
    position: absolute;
    right: 26px;
    bottom: 30px;
    width: 190px;
    text-align: center;
    color: #fff;
  }
  .back-name {
    font-weight: 500;
    font-size: 19px;
    letter-spacing: 0.5px;
  }
  .back-url {
    margin-top: 20px;
    font-size: 13px;
    letter-spacing: 1.5px;
  }
</style>
</head>
<body>

<section class="card card-front">
  <svg class="front-bands" viewBox="0 0 600 343" width="600" height="343" aria-hidden="true">
    <polygon points="0,0 600,0 600,2 0,42" fill="var(--brand-blue)"/>
    <polygon points="60,343 600,300 600,343" fill="var(--brand-grey)"/>
  </svg>

  <div class="brand-lockup">
    <span class="brand-dot"></span>
    <span class="brand-name">Vellum Systemics</span>
  </div>

  <div class="divider"></div>

  <div class="contact-block">
    <div class="person-name">DANIEL MARSH</div>
    <div class="person-title">CEO/FOUNDER</div>
    <div class="address">4210 Alder Crest Road<br>Juneau, Alaska 99801</div>
    <ul class="contact-list">
      <li>
        <svg viewBox="0 0 16 16"><path d="M3.5 1l2.5 3-1.5 2c.8 1.8 2.2 3.2 4 4l2-1.5 3 2.5-1.5 3C6.5 14 2 9.5 1 2.5z"/></svg>
        907 512 3846
      </li>
      <li>
        <svg viewBox="0 0 16 16"><path d="M4 0h8a1 1 0 0 1 1 1v14a1 1 0 0 1-1 1H4a1 1 0 0 1-1-1V1a1 1 0 0 1 1-1zm1 2v10h6V2zm3 11a1 1 0 1 0 0 2 1 1 0 0 0 0-2z"/></svg>
        907 274 6153
      </li>
      <li>
        <svg viewBox="0 0 16 16"><path d="M4 0h8v5H4zM1 6h14v7h-2v3H3v-3H1zm4 5v3h6v-3z"/></svg>
        907 338 5027
      </li>
      <li>
        <svg viewBox="0 0 16 16"><path d="M0 3h16v10H0zm1.5 1.2v.4L8 9l6.5-4.4v-.4z"/></svg>
        daniel@vellumsys.com
      </li>
      <li>
        <svg viewBox="0 0 16 16"><circle cx="8" cy="8" r="7.5"/><path d="M4 5c1 0 2 1 2 2s2 1 2 2-1 2 0 3M9 2c0 1 1 2 2 2s2 1 2 3" stroke="#f3f3f3" stroke-width="1.3" fill="none"/></svg>
        www.vellumsys.com
      </li>
    </ul>
  </div>
</section>

<section class="card card-back">
  <div class="back-lockup">
    <div class="back-name">Vellum Systemics</div>
    <div class="back-url">www.vellumsys.com</div>
  </div>
</section>

</body>
</html>
```